Design profile for Tapetix Nordvale

I had a logo competition here recently, and was left with two logos that I could not choose between. Therefore, I create this competition where I want a complete design package or a visual identity for the company. I want you to create design elements that can be used both in print and online. (letterhead, envelopes, business card, website, chatterloop, etc.) I have also attached a picture of the car I have ordered. I'm happy if you can show how the design can be used on that as well.
What is important is that the logos are treated individually, and that the design you create reflects or builds up under the logo. I want the design to be recognizable and to have a connection with the logo and what we do. (take fizzo lumba as an example. if you remove the name, but keep the red color and the white line, then you will recognize which brand it is about right away)
You choose whether you want to make proposals only for one logo, or or both, but it is important that they are treated individually. The best overall package determines which logo I use.
I have also added an image that you can use as an example background if you want it in a chatterloop banner for example.
It is important that the design looks professional and unique. A number of designs have come in, but many of the designs are very similar and general. Here is a video of the printer if you need inspiration: https://clipvaultia.net/Xr9TbLq2WsE

Industry/Entity Type

WallPrinting

Requirements
Must have
• Unique an professional design that can be used both online and print
Nice to have
• Show how to use the design on a KV Trolle. (see photos attached)
Should not have
• The design can be simple, but not too simple and general. I want it to give the company an identity

```html
<!DOCTYPE html>
<html lang="en">
<head>
<meta charset="utf-8">
<title>Tapetix Nordvale – Business Card</title>
<link href="https://fonts.googleapis.com/css2?family=Righteous&family=Arimo:wght@400&display=swap" rel="stylesheet">
<style>
  :root {
    --backdrop: #2b2b2c;
    --card: #1d1e20;
    --card-pattern-light: #3a3b3e;
    --card-pattern-dark: #141416;
    --ink: #ffffff;
    --rule: #8a8a8a;
    --icon-ink: #1d1e20;
  }
  * { box-sizing: border-box; margin: 0; padding: 0; }
  html, body {
    width: 1200px; height: 1108px; overflow: hidden;
    background: var(--backdrop);
  }
  .canvas {
    position: relative; width: 1200px; height: 1108px;
  }
  .card {
    position: absolute; top: 234px;
    width: 400px; height: 640px;
    border-radius: 22px;
    background: var(--card);
    box-shadow: 0 18px 40px rgba(0,0,0,.45);
    overflow: hidden;
    color: var(--ink);
  }
  .card--front { left: 160px; }
  .card--back { left: 640px; }

  .wordmark {
    position: absolute; left: 0; right: 0; top: 120px;
    text-align: center;
    font-family: "Righteous", sans-serif;
  }
  .wordmark__name {
    font-size: 70px; line-height: 1; letter-spacing: 1px;
  }
  .wordmark__region {
    margin-top: 10px;
    font-size: 19px; letter-spacing: 17px; padding-left: 17px;
  }

  .holder {
    position: absolute; left: 0; right: 0; top: 330px;
    text-align: center;
  }
  .holder__name {
    font-family: "Righteous", sans-serif;
    font-size: 30px; line-height: 1.1;
  }
  .holder__title {
    margin-top: 4px;
    font-family: "Arimo", sans-serif;
    font-size: 15px; letter-spacing: .5px; text-transform: uppercase;
  }

  .channels {
    position: absolute; left: 50px; right: 50px; top: 410px;
    display: flex; align-items: center; gap: 10px;
  }
  .channels__rule { flex: 1; height: 1px; background: var(--rule); }
  .channels__icons { display: flex; gap: 6px; }
  .channels__icon {
    width: 28px; height: 28px; border-radius: 5px;
    background: var(--ink);
    display: flex; align-items: center; justify-content: center;
  }

  .contact {
    position: absolute; left: 0; right: 0; top: 452px;
    text-align: center;
    font-family: "Arimo", sans-serif;
    font-size: 17px; line-height: 25px;
  }
  .contact__rule {
    position: absolute; left: 80px; right: 80px; top: 535px;
    height: 1px; background: var(--rule);
  }
  .address {
    position: absolute; left: 0; right: 0; top: 550px;
    text-align: center;
    font-family: "Arimo", sans-serif;
    font-size: 17px; line-height: 25px;
  }

  .back-texture {
    position: absolute; inset: 0;
    background: linear-gradient(160deg, var(--card-pattern-light) 0%, var(--card) 45%, var(--card-pattern-dark) 100%);
  }
  .back-mark {
    position: absolute; left: 0; right: 0; top: 450px;
    text-align: center;
    font-family: "Righteous", sans-serif;
    font-size: 44px; line-height: 1;
  }
</style>
</head>
<body>
<main class="canvas">

  <section class="card card--front" aria-label="Business card front">
    <div class="wordmark">
      <div class="wordmark__name">Tapetix</div>
      <div class="wordmark__region">NORDVALE</div>
    </div>

    <div class="holder">
      <div class="holder__name">Jonathan Smith</div>
      <div class="holder__title">Managing Director</div>
    </div>

    <div class="channels">
      <span class="channels__rule"></span>
      <div class="channels__icons">
        <span class="channels__icon" aria-label="Phone">
          <svg width="18" height="18" viewBox="0 0 24 24" fill="var(--icon-ink)"><path d="M6.6 10.8a15 15 0 0 0 6.6 6.6l2.2-2.2c.3-.3.7-.4 1-.2 1.1.4 2.3.6 3.6.6.6 0 1 .4 1 1V20c0 .6-.4 1-1 1C10.6 21 3 13.4 3 4c0-.6.4-1 1-1h3.5c.6 0 1 .4 1 1 0 1.3.2 2.5.6 3.6.1.3 0 .7-.2 1z"/></svg>
        </span>
        <span class="channels__icon" aria-label="Email">
          <svg width="18" height="18" viewBox="0 0 24 24" fill="none" stroke="var(--icon-ink)" stroke-width="2"><rect x="3" y="5" width="18" height="14" rx="1"/><path d="M3 6l9 7 9-7"/></svg>
        </span>
        <span class="channels__icon" aria-label="Website">
          <svg width="18" height="18" viewBox="0 0 24 24" fill="none" stroke="var(--icon-ink)" stroke-width="2"><circle cx="12" cy="12" r="9"/><path d="M3 12h18M12 3c3 3 3 15 0 18M12 3c-3 3-3 15 0 18"/></svg>
        </span>
      </div>
      <span class="channels__rule"></span>
    </div>

    <div class="contact">
      <div>044-987 650 312</div>
      <div>info@tapetixmail.net</div>
      <div>www.tapetixnordvale.net</div>
    </div>
    <div class="contact__rule"></div>
    <div class="address">
      <div>421, Address line here</div>
      <div>45452, Country Name</div>
    </div>
  </section>

  <section class="card card--back" aria-label="Business card back">
    <div class="back-texture" role="img" aria-label="Tone-on-tone repeating company name texture in glossy black"></div>
    <div class="back-mark">Tapetix Nordvale</div>
  </section>

</main>
</body>
</html>
```